Quorvex - Automated robotic Inspection with AI need new business cards

We need a new design of our business cards. The company is focused on automated quality control at high speed with unmatched results. We have a logo but need a more forward leaning business card that shows that we are delivering cutting edge technology.

Contact Information for Business Card

Name
Position
Adress
Phone
Email
e.g.
Lena Holmqvist
Chief Financial Officer (CFO)

Quorvex Sweden AB
Bruksvägen 14, SE-175 43 JÄRFÄLLA, Sweden
Mobile: +46735 21 47 83 | Office: +46 8 61 94 27
www.quorvex-example.com

Font styles to use
Sans Serif

```html
<!DOCTYPE html>
<html lang="en">
<head>
<meta charset="utf-8">
<title>Quorvex business cards</title>
<link rel="stylesheet" href="https://fonts.googleapis.com/css2?family=Arimo:wght@400;700&display=swap">
<style>
  :root {
    --brand-blue: #1b5a89;
    --brand-blue-deep: #174f7a;
    --card-white: #ffffff;
    --backdrop: #2b2e33;
    --text-blue: #1a5785;
  }
  * { box-sizing: border-box; margin: 0; padding: 0; }
  html, body {
    width: 1200px; height: 985px; overflow: hidden;
    background: var(--backdrop);
    font-family: "Arimo", Arial, sans-serif;
  }
  .stage {
    position: relative; width: 1200px; height: 985px;
    display: flex; align-items: center; justify-content: center; gap: 40px;
  }
  .card {
    position: relative; width: 520px; height: 298px;
    border-radius: 18px; overflow: hidden;
  }
  .card--front {
    background: var(--card-white); color: var(--text-blue);
    display: flex; flex-direction: column; align-items: center;
    padding-top: 38px; text-align: center;
  }
  .card--back {
    background: linear-gradient(135deg, var(--brand-blue) 0%, var(--brand-blue-deep) 100%);
    color: var(--card-white);
    display: flex; flex-direction: column; align-items: center; justify-content: center;
  }
  .brand { display: flex; align-items: center; gap: 12px; }
  .brand__dot {
    width: 22px; height: 22px; border-radius: 50%;
    background: currentColor;
  }
  .brand__name {
    font-weight: 700; font-size: 46px; letter-spacing: 2px; line-height: 1;
  }
  .brand__tagline {
    font-size: 15px; letter-spacing: 4px; margin-top: 10px; font-weight: 700;
  }
  .contact { margin-top: 24px; font-size: 12.5px; line-height: 1.45; }
  .contact__name { font-weight: 700; font-size: 19px; line-height: 1.2; }
  .contact__role { margin-bottom: 8px; }
  .contact__label { font-weight: 700; }
  .card--back .brand__name { font-size: 56px; }
  .card--back .brand__dot { width: 26px; height: 26px; }
</style>
</head>
<body>
<main class="stage">
  <section class="card card--front" aria-label="Business card front">
    <div class="brand">
      <span class="brand__dot"></span>
      <span class="brand__name">Quorvex</span>
    </div>
    <p class="brand__tagline">Automated Quality Control</p>
    <div class="contact">
      <p class="contact__name">Lena Holmqvist</p>
      <p class="contact__role">Chief Financial Officer (CFO)</p>
      <p>Quorvex Sweden AB</p>
      <p>Bruksvägen 14, SE-175 43 JÄRFÄLLA, Sweden</p>
      <p><span class="contact__label">Mobile:</span> +46735 21 47 83 | <span class="contact__label">Office:</span> +46 8 61 94 27</p>
      <p>www.quorvex-example.com</p>
    </div>
  </section>
  <section class="card card--back" aria-label="Business card back">
    <div class="brand">
      <span class="brand__dot"></span>
      <span class="brand__name">Quorvex</span>
    </div>
    <p class="brand__tagline">Automated Quality Control</p>
  </section>
</main>
</body>
</html>
```